"Beyond Marrow Cay" Fictional Book Cover

BEYOND MARROW CAY
By: Dale Pruitt

Here's the intro .

"It had been nearly forty years since Ted Larraby last went to the island from where he was raised. Three months earlier he never would have thought about ever coming back. But life is weird. Things happen quickly and plans change, especially when your very life is at stake. The reason he was going back wasn’t to see old friends...no, no, no. They’re all dead. Of all the kids he grew up with on the island who moved off, he’s the only one still alive. Why?"

Pretty much all just a Lumeno book, by the way.

Target Market(s)

fiction readers

Requirements
Must have
• Somewhat of a dark, mysterious cover is what I'd like to see. Use your imagination. I've never written a fiction book before so I'm very open to ideas

Needs to have my name, DALE PRUITT at the bottom. like my other books, all of which are non-fiction
Nice to have
• Mysterious is what I'm looking for. NOT A HORROR story though. More a guy who left the island years ago, but is being called back to escape the rat race of modern, consumerist culture.

Please remember this NEEDS to jump out as a thumbnail on Bookvale as people are browsing. Mainly the WORDS need to stick out. Lighter words on a say a blue background.

If you want to try to use the attached pic, or something like this, to reflect an island in the cover, that'd be good.

I've also uploaded a couple images I purchased from Pixelcrate, hopefully you can make something work with these.

```html
<!DOCTYPE html>
<html lang="en">
<head>
<meta charset="utf-8">
<title>Beyond Marrow Cay — Book Cover</title>
<link rel="stylesheet" href="https://fonts.googleapis.com/css2?family=Mrs+Saint+Delafield&family=Cormorant+Garamond:wght@500;600&family=EB+Garamond:wght@400;500&display=swap">
<style>
  :root {
    --backdrop: #e9e4dc;
    --paper-light: #f1e7a6;
    --paper-mid: #d9c67a;
    --paper-dark: #a98f48;
    --torn-edge: #5b4321;
    --ink: #1a140c;
    --scene-sky: #8c8a4e;
    --scene-trees: #3c4424;
    --scene-shore: #2a2d18;
    --night: #0b0b08;
    --author: #f6f1e4;
  }
  * { margin: 0; padding: 0; box-sizing: border-box; }
  html, body {
    width: 1200px;
    height: 1000px;
    overflow: hidden;
    background: var(--backdrop);
  }
  .canvas {
    position: relative;
    width: 1200px;
    height: 1000px;
  }
  .cover {
    position: absolute;
    left: 260px;
    top: 37px;
    width: 680px;
    height: 925px;
    overflow: hidden;
    background:
      radial-gradient(ellipse at 50% 30%, var(--paper-light) 0%, var(--paper-mid) 55%, var(--paper-dark) 100%);
  }
  .torn-edge {
    position: absolute;
    left: 0;
    top: 0;
    width: 680px;
    height: 90px;
  }
  .island-scene {
    position: absolute;
    left: 0;
    top: 470px;
    width: 680px;
    height: 455px;
    background: linear-gradient(180deg,
      rgba(140,138,78,0) 0%,
      var(--scene-sky) 10%,
      var(--scene-trees) 38%,
      #6f6a48 58%,
      var(--scene-shore) 78%,
      var(--night) 92%);
  }
  .title {
    position: absolute;
    left: 0;
    top: 108px;
    width: 680px;
    text-align: center;
    color: var(--ink);
  }
  .title-script {
    display: block;
    font-family: "Mrs Saint Delafield", cursive;
    font-size: 112px;
    line-height: 90px;
    margin-left: 20px;
  }
  .title-caps {
    display: block;
    font-family: "Cormorant Garamond", serif;
    font-weight: 500;
    font-size: 80px;
    line-height: 80px;
    letter-spacing: 1px;
  }
  .blurb {
    position: absolute;
    left: 80px;
    top: 302px;
    width: 520px;
    font-family: "EB Garamond", serif;
    font-size: 17.5px;
    line-height: 26px;
    text-align: center;
    color: var(--ink);
  }
  .author {
    position: absolute;
    left: 0;
    top: 838px;
    width: 680px;
    text-align: center;
    font-family: "Cormorant Garamond", serif;
    font-weight: 500;
    font-size: 62px;
    letter-spacing: 2px;
    color: var(--author);
  }
</style>
</head>
<body>
  <main class="canvas">
    <article class="cover">
      <svg class="torn-edge" viewBox="0 0 680 90" aria-hidden="true">
        <path d="M0 0 H680 V40 L640 52 L600 44 L560 58 L520 50 L470 62 L430 54 L380 66 L340 56 L300 64 L250 52 L210 60 L160 48 L120 56 L80 46 L40 54 L0 44 Z" fill="var(--torn-edge)" opacity="0.75"/>
      </svg>

      <div class="island-scene" role="img" aria-label="Photograph of an island shoreline with old clapboard houses among autumn trees and a pavilion on the water"></div>

      <h1 class="title">
        <span class="title-script">Beyond</span>
        <span class="title-caps">MARROW CAY</span>
      </h1>

      <p class="blurb">"It had been nearly forty years since Ted Larraby last went to the island from where he was raised. Three months earlier he never would have thought about ever coming back. But life is weird. Things happen quickly and plans change, especially when your very life is at stake. The reason he was going back wasn’t to see old friends...no, no, no. They’re all dead. Of all the kids he grew up with on the island who moved off, he’s the only one still alive. Why?"</p>

      <p class="author">DALE PRUITT</p>
    </article>
  </main>
</body>
</html>
```